B7k Website Design

We need a website design, look, feel and functionality that uses a recently approved logo attached. This should be a highly professional looking website that is relatively simple, but scalable. The website should carry information about the company, links and blog posts. The look and feel of the website should be consistent with the logo colour palette, but does not have to stick to them exactly. The company provides high quality brokering and support services for multinational companies to work with international humanitarian organisations and the Meridian Accord. Where possible, the design should make the most of the concept that collective action has a greater impact, and that Compass9Reach can help make that happen. The attached text can be used as a basis for the website text.

Target Market(s)

Heads of company foundations, and humanitarian organisations, and Meridian Accord departments the promote collaboration

Number of Pages Required

3 page

Requirements
Should not have
• Photos of people in suits.
• Photos of poor African children begging for help, or smiling in gratitude for aid

```html
<!DOCTYPE html>
<html lang="en">
<head>
<meta charset="utf-8">
<title>B7k — Compass 9 Reach</title>
<link rel="stylesheet" href="https://fonts.googleapis.com/css2?family=Open+Sans:wght@400;600;700&family=Montserrat:wght@800&display=swap">
<style>
  :root {
    --navy: #2b2a52;
    --ink: #333333;
    --frame: #e4e4e4;
    --page: #ffffff;
    --rule: #d6d6d6;
    --stone-light: #e9e2d6;
    --stone-mid: #b9ab94;
    --stone-dark: #4a443c;
  }
  * { margin: 0; padding: 0; box-sizing: border-box; }
  html, body { width: 1191px; height: 1200px; overflow: hidden; background: var(--frame); }
  .page {
    position: absolute; left: 14px; top: 14px; width: 1163px; height: 1172px;
    background: var(--page); font-family: "Open Sans", Arial, sans-serif; color: var(--ink);
  }
  .brand {
    position: absolute; left: 22px; top: 40px; display: flex; align-items: center; gap: 10px;
    font-family: "Open Sans", Arial, sans-serif; font-weight: 700; font-size: 42px; color: var(--navy);
  }
  .brand-dot { width: 18px; height: 18px; border-radius: 50%; background: var(--navy); }
  .info-bar {
    position: absolute; right: 24px; top: 0; width: 488px; height: 36px;
    background: var(--navy); clip-path: polygon(0 0, 100% 0, 96% 100%, 5% 100%);
    display: flex; align-items: center; gap: 10px; padding-left: 52px;
    color: #fff; font-weight: 700; font-size: 14.5px; letter-spacing: 0.2px;
  }
  .info-bar svg { flex: none; }
  .social { display: flex; gap: 4px; margin-left: 28px; }
  .social span { width: 22px; height: 22px; border: 1.5px solid #fff; border-radius: 50%; }
  .nav {
    position: absolute; right: 28px; top: 79px; display: flex; align-items: center; gap: 20px;
    font-weight: 700; font-size: 15px; color: var(--navy);
  }
  .nav a { color: inherit; text-decoration: none; padding: 6px 0; }
  .nav .current { border-bottom: 3px solid var(--navy); }
  .nav .contact { background: var(--navy); color: #fff; padding: 6px 10px; border-radius: 2px; }
  .hero {
    position: absolute; left: 0; top: 128px; width: 1163px; height: 549px;
    background:
      linear-gradient(180deg, rgba(255,255,255,0) 70%, rgba(60,55,50,0.55) 100%),
      linear-gradient(90deg, var(--stone-dark) 0%, #8e826f 20%, var(--stone-light) 45%, #d9cfbd 65%, var(--stone-mid) 100%);
    box-shadow: 0 14px 16px -10px rgba(0,0,0,0.35);
  }
  .title-row {
    position: absolute; left: 0; top: 730px; width: 1163px;
    display: flex; justify-content: center; align-items: center; gap: 28px;
  }
  .title-row .rule { width: 96px; height: 1px; background: var(--rule); }
  .title {
    font-family: "Montserrat", Arial, sans-serif; font-weight: 800; font-size: 24px;
    color: var(--navy); letter-spacing: 0.3px;
  }
  .intro {
    position: absolute; left: 72px; top: 806px; width: 1019px;
    font-size: 12.6px; line-height: 20px; text-align: center; color: #444;
  }
  .footer-brand {
    position: absolute; left: 0; top: 1032px; width: 1163px; display: flex; justify-content: center;
    align-items: center; gap: 10px; font-weight: 700; font-size: 42px; color: var(--navy);
  }
  .footer-rule { position: absolute; left: 0; top: 1121px; width: 1163px; height: 2px; background: #9a9a9a; }
  .copyright {
    position: absolute; left: 0; top: 1136px; width: 1163px; text-align: center;
    font-weight: 700; font-size: 11.5px; color: #555;
  }
</style>
</head>
<body>
<div class="page">
  <header>
    <div class="brand"><span class="brand-dot"></span>B7k</div>
    <div class="info-bar">
      <svg width="20" height="20" viewBox="0 0 20 20" aria-hidden="true">
        <circle cx="10" cy="10" r="9" fill="none" stroke="#fff" stroke-width="1.5"/>
        <path d="M7 5.5l1.5 2.2-1 1.2c.6 1.3 1.6 2.3 2.9 2.9l1.2-1 2.2 1.5-.8 1.6c-3.6-.3-6.5-3.2-6.8-6.8z" fill="#fff"/>
      </svg>
      <span>FOR INFORMATION : 123.456.7890</span>
      <div class="social" aria-label="Social links"><span></span><span></span><span></span></div>
    </div>
    <nav class="nav">
      <a class="current" href="#">HOME</a>
      <a href="#">ABOUT</a>
      <a href="#">SERVICES</a>
      <a href="#">NEWS</a>
      <a class="contact" href="#">CONTACT US</a>
    </nav>
  </header>

  <div class="hero" role="img" aria-label="Photograph of a historic city street lined with classical stone government buildings under a cloudy sky"></div>

  <section>
    <div class="title-row"><span class="rule"></span><h1 class="title">COMPASS 9 REACH</h1><span class="rule"></span></div>
    <p class="intro">Lorem ipsum dolor sit amet, consectetuer adipiscing elit, sed diam nonummy nibh euismod tincidunt ut laoreet dolore magna aliquam erat volutpat. Ut wisi enim ad minim veniam, quis nostrud exerci tation ullamcorper suscipit lobortis nisl ut aliquip ex ea commodo consequat. Duis autem vel eum iriure dolor in hendrerit in vulputate velit esse molestie consequat, vel illum dolore eu feugiat nulla facilisis at vero eros et accumsan et iusto odio dignissim qui blandit praesent luptatum zzril delenit augue duis dolore te feugait nulla facilisi. Nam liber tempor cum soluta nobis eleifend option congue nihil imperdiet doming id quod mazim placerat facer possim assum. Typi non habent claritatem insitam; est usus legentis in iis qui facit eorum claritatem. Investigationes demonstraverunt lectores legere me lius quod ii legunt saepius.</p>
  </section>

  <footer>
    <div class="footer-brand"><span class="brand-dot"></span>B7k</div>
    <div class="footer-rule"></div>
    <p class="copyright">© 2018COMPASS 9 REACH I ALL RIGHTS RESERVED</p>
  </footer>
</div>
</body>
</html>
```